Product labels for new supplements business targeting high performing creative people

I need a label design for different supplements like Whey, BCAA, Melatonin etc. that I could customize for each use case separately.

The brand is called wovenpath.life, and it would be the first design of the labels. We haven't sold any products yet, but the target audience is people with growth mindset, people who want to be as efficient as possible and are constantly looking to improve their lifestyle. As part of that, they are also working out, but don't know much about supplements yet. Mostly people between 20-34.

I don't have a too specific idea of the expected design, though it should be light, warm, smart and minimalist, maybe have some patterns. It should looks smart and clean (and expensive). Orange and golden might be the additional colors for white. I have attached the templates of some products that I plan to sell and also the logo of the brand.

Here's what I have used for inspiration:
Brands that I like and are somewhat similar in concept: https://www.plarnix.com/ (!!specially the way they
bring "how the product helps them" in focus, not "what the product is" & https://www.bevo.care/ &
https://www.moflesta.com/sport/ & https://en.calwostor.fr/ &
https://artboardhub.com/profiles/mirelfondastudio/designs/461827

Here's how different products look like: https://bondrexa.com/catalog

Target Market(s)

target audience is people with growth mindset, people who want to be as efficient as possible and are constantly looking to improve their lifestyle. As part of that, they are also working out, but don't know much about supplements yet. Mostly people between 20-34.

Industry/Entity Type

Supplements

Font styles to use
Sans Serif

Colors
FFC000
F8CF3A
FAE287
FDF2CF
FEFAEE
F0912C
F2A743
F7CA91
FBE8D2
FDF5EE
EE7325
F08F49
F5BC92
FAE3D3
FDF4ED

Requirements
Must have
• Clean, smart and minimalist design that can be applied for different products in different sizes, like Whey protein, BCAA, vitamins etc. available here: https://bondrexa.com/catalog
Nice to have
• Patterns, expensive look
Should not have
• Doodles, too many colors

```html
<!DOCTYPE html>
<html lang="en">
<head>
<meta charset="UTF-8">
<title>wovenpath.life — Maca Root Powder Label</title>
<link href="https://fonts.googleapis.com/css2?family=DM+Sans:wght@400;500&family=Montserrat:wght@800;900&display=swap" rel="stylesheet">
<style>
  :root {
    --page-bg: #fafbfc;
    --label-dark: #150c0c;
    --label-mid: #2c1d1d;
    --text-light: #f4f0ee;
    --accent-orange: #ee7325;
    --accent-warm: #f0912c;
  }
  * { margin: 0; padding: 0; box-sizing: border-box; }
  html, body {
    width: 1200px;
    height: 1000px;
    overflow: hidden;
    background: var(--page-bg);
  }
  .canvas {
    position: relative;
    width: 1200px;
    height: 1000px;
  }
  .label {
    position: absolute;
    left: 300px;
    top: 170px;
    width: 600px;
    height: 660px;
    background: linear-gradient(160deg, var(--label-mid) 0%, #241616 45%, var(--label-dark) 100%);
    color: var(--text-light);
    font-family: "DM Sans", sans-serif;
    overflow: hidden;
  }
  .brand {
    position: absolute;
    top: 80px;
    left: 0;
    width: 100%;
    display: flex;
    flex-direction: column;
    align-items: center;
    gap: 18px;
  }
  .brand-dot {
    width: 44px;
    height: 44px;
    border-radius: 50%;
    background: var(--accent-orange);
  }
  .brand-name {
    font-size: 30px;
    font-weight: 500;
    letter-spacing: 0.5px;
    color: var(--text-light);
  }
  .product-title {
    position: absolute;
    top: 248px;
    right: 100px;
    text-align: right;
  }
  .product-name {
    font-family: "Montserrat", sans-serif;
    font-weight: 900;
    font-size: 56px;
    letter-spacing: 1.5px;
    line-height: 1;
  }
  .product-form {
    margin-top: 10px;
    font-family: "DM Sans", sans-serif;
    font-weight: 500;
    font-size: 34px;
    letter-spacing: 3px;
    line-height: 1;
  }
  .accent-area {
    position: absolute;
    left: 178px;
    top: 384px;
    width: 36px;
    height: 156px;
    background: linear-gradient(180deg, var(--accent-warm) 0%, var(--accent-orange) 100%);
    opacity: 0.9;
  }
  .benefits {
    position: absolute;
    left: 240px;
    top: 430px;
    font-size: 20px;
    line-height: 1.3;
    letter-spacing: 0.8px;
    list-style: none;
  }
  .label-footer {
    position: absolute;
    bottom: 60px;
    left: 112px;
    right: 130px;
    display: flex;
    justify-content: space-between;
    font-size: 21px;
    letter-spacing: 1px;
  }
</style>
</head>
<body>
  <main class="canvas">
    <section class="label">
      <header class="brand">
        <span class="brand-dot"></span>
        <span class="brand-name">wovenpath.life</span>
      </header>

      <div class="product-title">
        <h1 class="product-name">MACA ROOT</h1>
        <p class="product-form">POWDER</p>
      </div>

      <div class="accent-area" role="img" aria-label="Orange angular accent graphic beside the benefit list"></div>

      <ul class="benefits">
        <li>Helps reduce stress*</li>
        <li>Increases energy and</li>
        <li>stamina*</li>
      </ul>

      <footer class="label-footer">
        <span class="supplement-type">DIETARY SUPPLEMENT</span>
        <span class="net-weight">200g</span>
      </footer>
    </section>
  </main>
</body>
</html>
```